Harbor Quill is a Smart Device and Wiring Business offering the latest in Smart Home Devices inc

Looking for a new website to draw people to my business and explain what a smart home is all about. I currently own a domain and have a website I put together in webnimbus business website builder. address www.harborquill.com. The website needs modernising and be visually appealing with cool action buttons, client feedback page etc.

The webpage needs to present an image of seamless integration of wireless voice control and smart devices that take tasks and activities away from the owner saving them time and money.

I have a chatterbay business page(harbor quill) and snapmeadow linked with the business, are we able to link this to the website somehow?

Target Market(s)

Residential home owners who want to modernise their home. Who have seen adverts for orbit nook and kestrel nova and want to put it in their home.

Industry/Entity Type

Technology Equipment

Number of Pages Required

1 page

Colors

Designer to choose colors to be used in the design.

Requirements
Must have
• A great landing page, that is modern and attractive, that gets across the idea of smart devices and technology.
• Must be ios/android device friendly.
Nice to have
• interactive/animated buttons
• I like the direction and interactiveness of these websites, a simplified version would be awesome.
• Something in between:
• http://www.oakridgelofts.com/ and https://plumcove.com/
• http://www.oakridgelofts.com/

```html
<!DOCTYPE html>
<html lang="en">
<head>
<meta charset="utf-8">
<title>Harbor Quill — Smart Device Integration</title>
<link rel="stylesheet" href="https://fonts.googleapis.com/css2?family=Jost:wght@400;500;600&display=swap">
<style>
:root{
  --brand:#1c9fdc;
  --brand-deep:#0a6bb5;
  --cyan:#00bcef;
  --ink:#222831;
  --muted:#5a5f66;
  --ring:#c9d3da;
  --footer:#101215;
  --white:#ffffff;
}
*{margin:0;padding:0;box-sizing:border-box}
html,body{width:1200px;height:2671px;overflow:hidden}
body{position:relative;font-family:"Jost",sans-serif;color:var(--ink);background:var(--white)}
.abs{position:absolute}

/* header */
.site-header{position:absolute;left:0;top:0;width:1200px;height:96px;background:var(--white);border-top:3px solid var(--brand)}
.brand{position:absolute;left:22px;top:28px;display:flex;align-items:center;gap:10px}
.brand-dot{width:34px;height:34px;border-radius:50%;background:var(--brand)}
.brand-name{font-size:26px;font-weight:600;color:var(--ink);letter-spacing:.5px}
.main-nav{position:absolute;left:306px;top:38px;display:flex;gap:26px;font-size:13px}
.main-nav a{color:var(--ink);text-decoration:none}
.main-nav a.active{color:var(--brand)}
.header-phone{position:absolute;left:820px;top:30px;display:flex;align-items:center;gap:12px;color:var(--brand);font-size:26px}
.quick-contact{position:absolute;left:1049px;top:32px;width:128px;height:38px;background:var(--brand);color:var(--white);font-size:12px;font-weight:500;display:flex;align-items:center;justify-content:center}

/* hero */
.hero{position:absolute;left:0;top:96px;width:1200px;height:550px}
.hero-photo{position:absolute;inset:0;background:linear-gradient(100deg,#5a4632 0%,#a08763 30%,#c9b08a 48%,#6f89a8 70%,#4a6f9a 100%)}
.hero-copy{position:absolute;left:666px;top:120px;color:var(--white);width:400px}
.eyebrow{font-size:15px;font-weight:500;letter-spacing:.3px}
.hero-title{font-size:46px;font-weight:400;line-height:1.14;margin-top:16px}
.hero-text{font-size:14px;line-height:1.4;margin-top:18px;width:390px}
.btn{display:inline-flex;align-items:center;justify-content:center;background:var(--brand);color:var(--white);font-weight:600}
.hero-btn{position:absolute;left:666px;top:449px;width:135px;height:38px;font-size:11px;gap:14px}

/* about */
.about{position:absolute;left:0;top:646px;width:1200px;height:579px}
.about-photo{position:absolute;inset:0;background:linear-gradient(90deg,#1668b8 0%,#2a84cc 45%,#1f73c0 75%,#0f5fae 100%)}
.about-frame{position:absolute;left:119px;top:123px;width:130px;height:333px;border:1.5px solid rgba(255,255,255,.85);border-right:none}
.about-copy{position:absolute;left:208px;top:170px;color:var(--white);width:420px}
.about-eyebrow{font-size:22px;font-weight:600}
.about-title{font-size:42px;font-weight:400;margin-top:4px;letter-spacing:.5px}
.about-text{font-size:14px;line-height:1.4;margin-top:10px;width:400px}
.about-btn{position:absolute;left:212px;top:390px;width:89px;height:24px;font-size:9px}

/* services */
.services-title{position:absolute;left:0;top:1345px;width:1200px;text-align:center;font-size:38px;font-weight:400;color:var(--brand)}
.services-sub{position:absolute;left:0;top:1396px;width:1200px;text-align:center;font-size:14px;line-height:1.3;color:var(--muted)}
.service{position:absolute;width:220px;text-align:center}
.service-ring{width:214px;height:214px;margin:0 auto;border-radius:50%;background:var(--ring);border:2px solid #e8eef2;display:flex;align-items:center;justify-content:center}
.service-disc{width:196px;height:196px;border-radius:50%;display:flex;align-items:center;justify-content:center}
.disc-cyan{background:var(--cyan)}
.disc-deep{background:var(--brand-deep)}
.service-label{font-size:14px;margin-top:20px;color:var(--ink)}

/* call band */
.call-band{position:absolute;left:0;top:2156px;width:1200px;height:132px;background:linear-gradient(100deg,#17a6e3 0%,#1a9ad9 60%,#0f8acb 100%);color:var(--white)}
.call-text{position:absolute;left:170px;top:30px;width:340px;text-align:center;font-size:25px;line-height:1.28}
.call-number{position:absolute;left:514px;top:22px;font-size:72px;font-weight:400;letter-spacing:1px}

/* footer */
.site-footer{position:absolute;left:0;top:2288px;width:1200px;height:383px;background:var(--footer);color:var(--white);font-size:11.5px;border-top:1px solid #2a2d33}
.footer-links{position:absolute;left:126px;top:66px;list-style:none;line-height:22.5px}
.footer-heading{position:absolute;font-size:11.5px}
.social{position:absolute;left:281px;top:96px;display:flex;gap:6px}
.social span{width:32px;height:32px;background:var(--white);display:block}
.footer-contact{position:absolute;left:281px;top:148px;line-height:17px;font-size:11px}
.field{position:absolute;left:593px;width:212px;border:1px solid #5a5f66;background:#0b0c0e;padding:5px 10px;font-size:11px}
.submit{position:absolute;left:593px;top:237px;width:91px;height:37px;font-size:11px}
.copyright{position:absolute;left:896px;top:66px;font-size:11px}
</style>
</head>
<body>

<header class="site-header">
  <div class="brand"><span class="brand-dot"></span><span class="brand-name">Harbor Quill</span></div>
  <nav class="main-nav">
    <a class="active">Home</a><a>What we do</a><a>Products</a><a>About</a><a>Contact</a>
  </nav>
  <div class="header-phone">
    <svg width="22" height="22" viewBox="0 0 22 22"><circle cx="11" cy="11" r="11" fill="var(--brand)"/><rect x="7.5" y="5" width="7" height="12" rx="1.5" fill="#fff"/><rect x="8.5" y="6.5" width="5" height="8" fill="var(--brand)"/></svg>
    <span>0488 310 527</span>
  </div>
  <div class="quick-contact">Quick Contact</div>
</header>

<section class="hero">
  <div class="hero-photo" role="img" aria-label="Bright living room with a hand holding a phone showing a smart home control app"></div>
  <div class="hero-copy">
    <p class="eyebrow">SMART HOME</p>
    <h1 class="hero-title">SMART DEVICE<br>INTEGRATION</h1>
    <p class="hero-text">We are focused on delivering affordable and easily usable devices for your home and office. Wireless smart home - no need for pre-wired cabling</p>
  </div>
  <div class="btn hero-btn">LEARN MORE
    <svg width="7" height="10" viewBox="0 0 7 10"><path d="M1 1l4 4-4 4" stroke="#fff" stroke-width="1.8" fill="none"/></svg>
  </div>
</section>

<section class="about">
  <div class="about-photo" role="img" aria-label="Blue-toned office scene of a person using a phone beside a laptop"></div>
  <div class="about-frame"></div>
  <div class="about-copy">
    <p class="about-eyebrow">ABOUT</p>
    <h2 class="about-title">HARBOR QUILL</h2>
    <p class="about-text">Harbor Quill began as an idea in a garage and a belief that home technology should be readily available and reasonably priced. We are constantly sourcing and experimenting with new technologies and solutions to create any vision of the future you can imagine.</p>
  </div>
  <div class="btn about-btn">Learn More</div>
</section>

<h2 class="services-title">SMART DEVICE INTEGRATION</h2>
<p class="services-sub">how we can help you take full advantage of your smart Assistant<br>and control your home</p>

<div class="service" style="left:116px;top:1483px">
  <div class="service-ring"><div class="service-disc disc-cyan">
    <svg width="70" height="70" viewBox="0 0 70 70" fill="#fff"><path d="M24 14l34-6v40h-5V17l-24 4v31h-5z"/><ellipse cx="19" cy="52" rx="9" ry="7"/><ellipse cx="50" cy="48" rx="9" ry="7"/></svg>
  </div></div>
  <p class="service-label">Multi-Room Audio</p>
</div>
<div class="service" style="left:365px;top:1483px">
  <div class="service-ring"><div class="service-disc disc-deep">
    <svg width="70" height="70" viewBox="0 0 70 70" fill="none" stroke="#fff" stroke-width="4"><rect x="27" y="6" width="16" height="32" rx="8" fill="#fff"/><path d="M19 32c0 9 7 16 16 16s16-7 16-16M35 48v12M25 62h20"/></svg>
  </div></div>
  <p class="service-label">Voice Assistant</p>
</div>
<div class="service" style="left:615px;top:1483px">
  <div class="service-ring"><div class="service-disc disc-cyan">
    <svg width="70" height="70" viewBox="0 0 70 70"><rect x="9" y="18" width="52" height="8" fill="#fff"/><path d="M14 26h42c0 12-9 22-21 22S14 38 14 26z" fill="#fff"/><circle cx="35" cy="35" r="8" fill="var(--cyan)"/><circle cx="35" cy="35" r="4" fill="#fff"/></svg>
  </div></div>
  <p class="service-label">Smart CCTV</p>
</div>
<div class="service" style="left:862px;top:1483px">
  <div class="service-ring"><div class="service-disc disc-deep">
    <svg width="70" height="70" viewBox="0 0 70 70" fill="none" stroke="#fff" stroke-width="6" stroke-linecap="round"><path d="M23 20a20 20 0 1 0 24 0"/><path d="M35 10v24"/></svg>
  </div></div>
  <p class="service-label">Smart Blinds</p>
</div>

<div class="service" style="left:116px;top:1784px">
  <div class="service-ring"><div class="service-disc disc-deep">
    <svg width="70" height="70" viewBox="0 0 70 70" stroke="#fff" stroke-width="3" stroke-linecap="round"><path d="M35 4v7M13 14l5 5M57 14l-5 5M6 34h7M57 34h7M16 52l4-4M54 52l-4-4"/><path d="M24 33a11 11 0 1 1 22 0c0 6-5 8-5 14H29c0-6-5-8-5-14z" fill="#fff"/><path d="M29 52h12M30 57h10"/></svg>
  </div></div>
  <p class="service-label">Lighting Control</p>
</div>
<div class="service" style="left:365px;top:1784px">
  <div class="service-ring"><div class="service-disc disc-cyan">
    <svg width="70" height="70" viewBox="0 0 70 70"><path d="M24 32v-8a11 11 0 0 1 22 0v8" stroke="#fff" stroke-width="5" fill="none"/><rect x="19" y="31" width="32" height="27" rx="2" fill="#fff"/><circle cx="35" cy="42" r="3.5" fill="var(--cyan)"/><rect x="33.5" y="43" width="3" height="8" fill="var(--cyan)"/></svg>
  </div></div>
  <p class="service-label">Smart Lock</p>
</div>
<div class="service" style="left:615px;top:1784px">
  <div class="service-ring"><div class="service-disc disc-deep">
    <svg width="70" height="70" viewBox="0 0 70 70" fill="none" stroke="#fff" stroke-width="2.5"><rect x="21" y="6" width="28" height="58" rx="2"/><rect x="27" y="13" width="16" height="12"/><g fill="#fff" stroke="none"><rect x="27" y="31" width="4" height="4"/><rect x="33" y="31" width="4" height="4"/><rect x="39" y="31" width="4" height="4"/><rect x="27" y="38" width="4" height="4"/><rect x="33" y="38" width="4" height="4"/><rect x="39" y="38" width="4" height="4"/><rect x="27" y="45" width="4" height="4"/><rect x="33" y="45" width="4" height="4"/><rect x="39" y="45" width="4" height="4"/><rect x="27" y="52" width="16" height="4"/></g></svg>
  </div></div>
  <p class="service-label">Video Doorbell</p>
</div>
<div class="service" style="left:862px;top:1784px">
  <div class="service-ring"><div class="service-disc disc-cyan">
    <svg width="70" height="70" viewBox="0 0 70 70" fill="none" stroke="#fff" stroke-width="5" stroke-linecap="round"><path d="M11 30a34 34 0 0 1 48 0M19 38a22 22 0 0 1 32 0M27 46a10 10 0 0 1 16 0"/><circle cx="35" cy="53" r="3" fill="#fff"/></svg>
  </div></div>
  <p class="service-label">Smart Garage</p>
</div>

<section class="call-band">
  <p class="call-text">Contact us to and out how<br>we can help you</p>
  <p class="call-number">0488 310 527</p>
</section>

<footer class="site-footer">
  <ul class="footer-links">
    <li>Home</li><li>What we do</li><li>Products</li><li>About</li><li>Contact</li>
  </ul>
  <p class="footer-heading" style="left:281px;top:66px">Stay Connected</p>
  <div class="social"><span></span><span></span><span></span><span></span></div>
  <div class="footer-contact">
    <p>Email : info@harborquill.com.au</p>
    <p>Web : www.harborquill.com.au</p>
  </div>
  <p class="footer-heading" style="left:591px;top:66px">Get in touch</p>
  <div class="field" style="top:94px;height:25px">Your name</div>
  <div class="field" style="top:124px;height:25px">Email</div>
  <div class="field" style="top:155px;height:71px">Message</div>
  <div class="btn submit">SUBMIT</div>
  <p class="copyright">Allright reserved copyrith © 2018</p>
</footer>

</body>
</html>
```